Business Card Design

Target Market(s)

ORVAN is a huge indoor horse sports centre, so horse folks, equestrian, rodeo, western performance, breeds etc.....

Industry/Entity Type

Business

Contact Information for Business Card

O.R.V.A.N.
CHAPLAIN
Colin Marsday
colin@pwqvanlow.org
02 58314729 / 0438271605
Weddings, funerals,
general welfare, referrals,
personal development

Requirements
Nice to have
• something horsey on there but not cheesy!

```html
<!DOCTYPE html>
<html lang="en">
<head>
<meta charset="utf-8">
<title>O.R.V.A.N. Chaplain – Business Card</title>
<link rel="stylesheet" href="https://fonts.googleapis.com/css2?family=Jost:wght@300;400;500&display=swap">
<style>
  :root {
    --backdrop: #e9e8e6;
    --card: #ffffff;
    --ink: #111111;
    --ink-soft: #555555;
    --brand-purple: #2e2a55;
    --brand-gold: #f2c14e;
    --horse-gold: #f7e2a6;
  }
  * { box-sizing: border-box; margin: 0; padding: 0; }
  html, body {
    width: 1200px; height: 800px; overflow: hidden;
    background: var(--backdrop);
    font-family: "Jost", "Futura", sans-serif;
  }
  .canvas {
    width: 1200px; height: 800px;
    display: flex; align-items: center; justify-content: center;
  }
  .business-card {
    position: relative;
    width: 900px; height: 514px;
    background: var(--card);
    box-shadow: 0 10px 30px rgba(0,0,0,0.12);
  }
  .brand {
    position: absolute; left: 250px; top: 62px; width: 420px;
    display: flex; align-items: center; gap: 14px;
  }
  .brand-square {
    width: 26px; height: 26px; flex: none;
    background: var(--brand-purple);
  }
  .brand-name {
    font-weight: 500; font-size: 20px; line-height: 1.2;
    color: var(--brand-purple);
  }
  .role-title {
    position: absolute; left: 0; right: 0; top: 142px;
    text-align: center; padding-left: 20px;
    font-weight: 500; font-size: 42px; letter-spacing: 2px;
    color: var(--ink);
  }
  .person-name {
    position: absolute; left: 0; right: 0; top: 208px;
    text-align: center; padding-left: 20px;
    font-weight: 300; font-size: 36px;
    color: var(--ink-soft);
  }
  .contact-list {
    position: absolute; left: 64px; top: 282px;
    list-style: none;
  }
  .contact-item {
    display: flex; align-items: center; gap: 12px;
    font-weight: 400; font-size: 32px; line-height: 46px;
    color: var(--ink);
  }
  .contact-icon {
    width: 22px; height: 22px; flex: none;
    color: var(--brand-purple);
  }
  .services {
    position: absolute; left: 64px; right: 40px; top: 446px;
    font-weight: 300; font-size: 23px;
    color: var(--ink);
  }
  .horse-motif {
    position: absolute; left: 700px; top: 180px;
    width: 140px; height: 140px;
    border-radius: 50%;
    background: radial-gradient(circle, var(--horse-gold) 0%, rgba(247,226,166,0.25) 70%, rgba(255,255,255,0) 100%);
  }
</style>
</head>
<body>
<main class="canvas">
  <article class="business-card">
    <header class="brand">
      <span class="brand-square"></span>
      <span class="brand-name">Oakridge Rural Venue and Arena Network</span>
    </header>

    <h1 class="role-title">O.R.V.A.N. CHAPLAIN</h1>
    <p class="person-name">Colin Marsday</p>

    <ul class="contact-list">
      <li class="contact-item">
        <svg class="contact-icon" viewBox="0 0 24 24" aria-hidden="true">
          <circle cx="12" cy="12" r="4" fill="none" stroke="currentColor" stroke-width="2"/>
          <path d="M16 8v5a3 3 0 0 0 6 0v-1a10 10 0 1 0-4 8" fill="none" stroke="currentColor" stroke-width="2"/>
        </svg>
        colin@pwqvanlow.org
      </li>
      <li class="contact-item">
        <svg class="contact-icon" viewBox="0 0 24 24" aria-hidden="true">
          <path d="M6.6 10.8a15 15 0 0 0 6.6 6.6l2.2-2.2a1 1 0 0 1 1-.25 11.4 11.4 0 0 0 3.6.57 1 1 0 0 1 1 1V20a1 1 0 0 1-1 1A17 17 0 0 1 3 4a1 1 0 0 1 1-1h3.5a1 1 0 0 1 1 1c0 1.25.2 2.45.57 3.57a1 1 0 0 1-.25 1z" fill="none" stroke="currentColor" stroke-width="1.8"/>
        </svg>
        02 58314729
      </li>
      <li class="contact-item">
        <svg class="contact-icon" viewBox="0 0 24 24" aria-hidden="true">
          <path d="M6.6 10.8a15 15 0 0 0 6.6 6.6l2.2-2.2a1 1 0 0 1 1-.25 11.4 11.4 0 0 0 3.6.57 1 1 0 0 1 1 1V20a1 1 0 0 1-1 1A17 17 0 0 1 3 4a1 1 0 0 1 1-1h3.5a1 1 0 0 1 1 1c0 1.25.2 2.45.57 3.57a1 1 0 0 1-.25 1z" fill="none" stroke="currentColor" stroke-width="1.8"/>
        </svg>
        0438271605
      </li>
    </ul>

    <div class="horse-motif" role="img" aria-label="Gold line drawing of a horse's head"></div>

    <p class="services">Weddings, funerals, general welfare, referrals, personal development.</p>
  </article>
</main>
</body>
</html>
```